Wine label for new boutique South African wine focused on the USA market.

Wine label required for new ethical south African red wine called VELMO which stands for 'Pritchard, holloway, mabry and you' but is also a play on 'SA' and that it has a story to tell. Douglas Pritchard is the wine maker, Holloway the farm owner, and Mabry an investor.

Concept is a simple old type writer font on a white/off white label. Front label would say 'Velmo No.1, 2010 Shiraz, South Africa' and similarly a second for another wine 'Velmo No.2, 2010 Cab/Merlot Blend. Maybe the round stain of the bottom of a wine bottle in the bottom corner? Would also like for the 'velmo' to double up as the logo and work in the form of a stamp.

The rear label will need to tell a short story and be able to accommodate the usual boilerplate info. The story will go something like, ' Velmo No.1: It's a long story, but in short we love our wine and we think you will too. The cooling see breezes of the Indian Ocean help define this world class Shiraz from the Western Cape. Aged in french oak for 20 months, the bold flavors will compliment all red meats or simply enjoy on its own. Learn more about our story at www.velmowines-demo.com.

The cab/merlot will read similar: Velmo No.2: It's a long story, but in short we love our wine and we think you will too. The cooling see breezes of the Indian Ocean help define this world class red blend from the Western Cape. Aged in french oak for 20 months, this wine will compliment all red meats or simply enjoy on its own. Learn more about our story at www.velmowines-demo.com.

Reason: Had some great designs already, but as i get to understand how PitchLoom works, I'm keen to explore as many ideas as possible. Neil

Thanks for all the great designs everybody!

We will make a tough decision in the next couple of days.

Regards

Neil

Middle class with some wine knowledge. Price point around $20 -30

Boutique

• A small nod to the wine coming from south Africa in the design would be nice but nothing to over the top
• Simple and clear font with plenty of empty space on the label

```html
<!DOCTYPE html>
<html lang="en">
<head>
<meta charset="utf-8">
<title>Velmo Wine Labels</title>
<link rel="stylesheet" href="https://fonts.googleapis.com/css2?family=Courier+Prime:wght@400;700&family=Arvo:wght@700&family=Cormorant+Garamond:wght@500&display=swap">
<style>
  :root {
    --canvas: #ffffff;
    --label-paper: #fdfcf4;
    --ink: #1d1c1c;
    --band: #231f20;
    --gold: #f2a73b;
    --band-gold: #d9a24a;
  }
  * { margin: 0; padding: 0; box-sizing: border-box; }
  html, body {
    width: 1200px;
    height: 900px;
    overflow: hidden;
    background: var(--canvas);
  }
  .canvas {
    position: relative;
    width: 1200px;
    height: 900px;
    display: flex;
    justify-content: center;
    align-items: center;
    gap: 60px;
  }
  .front-label {
    position: relative;
    width: 460px;
    height: 460px;
    background: var(--label-paper);
    box-shadow: 3px 4px 8px rgba(0, 0, 0, 0.22);
    color: var(--ink);
  }
  .brand-name {
    position: absolute;
    top: 44px;
    left: 0;
    right: 0;
    text-align: center;
    font-family: "Courier Prime", monospace;
    font-weight: 400;
    font-size: 52px;
    letter-spacing: 12px;
    padding-left: 12px;
    color: var(--gold);
    line-height: 1;
  }
  .wine-number {
    position: absolute;
    left: 0;
    right: 0;
    display: flex;
    justify-content: center;
    align-items: flex-end;
    gap: 4px;
    margin-left: -30px;
  }
  .wine-number .number-prefix {
    font-family: "Arvo", serif;
    font-weight: 700;
    font-size: 22px;
    text-decoration: underline;
    text-underline-offset: 4px;
    text-decoration-thickness: 2px;
    margin-bottom: 70px;
  }
  .wine-number .number-digit {
    font-family: "Arvo", serif;
    font-weight: 700;
    font-size: 140px;
    line-height: 0.78;
  }
  .label-one .wine-number { top: 172px; }
  .label-two .wine-number { top: 150px; }
  .varietal {
    position: absolute;
    left: 0;
    right: 0;
    text-align: center;
    font-family: "Courier Prime", monospace;
    font-weight: 700;
    font-size: 19px;
    letter-spacing: 7px;
    padding-left: 7px;
  }
  .vintage {
    position: absolute;
    left: 0;
    right: 0;
    text-align: center;
    font-family: "Courier Prime", monospace;
    font-size: 19px;
    letter-spacing: 4px;
    padding-left: 4px;
  }
  .label-one .varietal { top: 318px; }
  .label-one .vintage { top: 354px; }
  .label-two .varietal { top: 312px; }
  .label-two .vintage { top: 348px; }
  .origin-band {
    position: absolute;
    left: 0;
    right: 0;
    bottom: 0;
    height: 56px;
    background: var(--band);
    display: flex;
    align-items: center;
    justify-content: center;
    font-family: "Cormorant Garamond", serif;
    font-weight: 500;
    font-size: 17px;
    letter-spacing: 5px;
    padding-left: 5px;
    color: var(--band-gold);
  }
</style>
</head>
<body>
  <main class="canvas">
    <section class="front-label label-one">
      <div class="brand-name">VELMO</div>
      <div class="wine-number"><span class="number-prefix">No.</span><span class="number-digit">1</span></div>
      <div class="varietal">SHIRAZ</div>
      <div class="vintage">2010</div>
      <div class="origin-band">WINE OF SOUTH AFRICA</div>
    </section>
    <section class="front-label label-two">
      <div class="brand-name">VELMO</div>
      <div class="wine-number"><span class="number-prefix">No.</span><span class="number-digit">2</span></div>
      <div class="varietal">CABERNET MERLOT</div>
      <div class="vintage">2010</div>
      <div class="origin-band">WINE OF SOUTH AFRICA</div>
    </section>
  </main>
</body>
</html>
```